Interior designer needs a power point template design

I need a template PowerPoint design for my client presentations. The presentations I prepare for my clients usually include the furniture project, the detail of the selected furniture, and the costs. There are a lot of images I insert. What I need is to have a template that I can use for all my presentations, where from time to time I will insert the specific images and descriptions I want to insert. What will always be the same will be the cover, the colors, the font, and the design of the internal sections.
I already have my logo that I would like to insert on each page of the presentation (in small size).
In summary, I need:
- basic template design
- cover with an image chosen by Picsmeadow photo
- design an internal section/chapter
- internal page design.

I like the clolors of pink and brown <8please see image attached)
Images (will come from Picsmeadow photo)
● entrance/hall
● living room
● dining room
● Bathroom
● Closet
● Kids room
● Master bedroom
● Master bathroom
● Kitchen
● Office
● Laundry
● Balcony or Terrace

Target Market(s)

Customers (both residential and commercial projects)

Industry/Entity Type

interior design

Font styles to use
Other font styles liked:
• I like courier new

Requirements
Must have
• beautiful design
Should not have
• animations

```html
<!DOCTYPE html>
<html lang="it">
<head>
<meta charset="utf-8">
<title>Template presentazione interior design</title>
<link rel="stylesheet" href="https://fonts.googleapis.com/css2?family=Open+Sans:wght@400;500;600&display=swap">
<style>
:root{
  --brown:#6d2d0d;
  --pink:#b77866;
  --white:#ffffff;
  --page:#ffffff;
  --ink:#5a3526;
  --ink-light:#f3e6df;
  --logo-grey:#8a8a8a;
}
*{margin:0;padding:0;box-sizing:border-box}
html,body{width:1200px;height:4051px;overflow:hidden;background:var(--page)}
body{position:relative;font-family:"Open Sans",Arial,sans-serif}
.slide{position:absolute;left:77px;width:1044px;height:587px;overflow:hidden;box-shadow:0 1px 4px rgba(0,0,0,.12)}
.abs{position:absolute}
.bg-brown{background:var(--brown)}
.bg-pink{background:var(--pink)}
.bg-white{background:var(--white)}
.title{font-weight:500;letter-spacing:.5px;color:var(--white);text-transform:uppercase}
.title-sm{font-size:22px}
.title-lg{font-size:34px;line-height:44px}
.vertical-title{font-weight:500;font-size:29px;line-height:31px;color:var(--brown);text-transform:uppercase;writing-mode:vertical-rl;transform:rotate(180deg);text-align:left}
.body-text{font-size:12.3px;line-height:23px;text-align:justify}
.body-text p+p{margin-top:18px}
.text-light{color:var(--ink-light)}
.text-dark{color:var(--ink)}
.photo{border:6px solid var(--white)}
.photo-plain{border:none}
.logo{position:absolute;top:10px;width:60px;display:flex;flex-direction:column;align-items:center;gap:6px}
.logo .mark{width:38px;height:38px;border-radius:50%;border:1.5px solid currentColor}
.logo .name{font-size:11px;font-weight:400;letter-spacing:1px;text-align:center;line-height:13px;text-transform:uppercase}
.logo-light{color:var(--ink-light)}
.logo-dark{color:var(--logo-grey)}
</style>
</head>
<body>

<!-- Slide 1 -->
<section class="slide bg-brown" style="top:90px">
  <h2 class="abs title title-sm" style="left:58px;top:44px">Camera padronale</h2>
  <div class="abs photo" role="img" aria-label="Illustrazione di una camera da letto con letto rosa, tende arancioni, toeletta e armadio" style="left:60px;top:116px;width:642px;height:417px;background:linear-gradient(180deg,#b9cfd2 0%,#a9c4c6 60%,#d9a08a 80%,#c5b7a7 100%)"></div>
  <div class="logo logo-light" style="left:925px"><span class="mark"></span><span class="name">Casa<br>Lumo</span></div>
  <div class="abs body-text text-light" style="left:740px;top:166px;width:244px">
    <p>L'arredamento della camera padronale. Sed ut perspiciatis unde omnis iste natus error sit voluptatem accusantium doloremque laudantium, totam rem aperiam, eaque ipsa quae ab illo inventore veritatis et quasi architecto beatae vitae dicta sunt explicabo. Nemo enim ipsam voluptatem quia voluptas sit aspernatur aut odit aut fugit.</p>
    <p>Sed ut perspiciatis unde omnis iste natus error sit voluptatem accusantium doloremque laudantium, totam rem aperiam, eaque ipsa quaea.</p>
  </div>
</section>

<!-- Slide 2 -->
<section class="slide bg-white" style="top:739px">
  <div class="abs bg-pink" style="left:343px;top:0;width:701px;height:293px"></div>
  <div class="abs photo-plain" role="img" aria-label="Illustrazione di un soggiorno con divano bordeaux, pianta e libreria" style="left:343px;top:60px;width:368px;height:467px;background:linear-gradient(180deg,#efe1d3 0%,#ecdccc 68%,#c98f5c 72%,#d59b64 100%)"></div>
  <h2 class="abs vertical-title" style="left:860px;bottom:60px">Cabina<br>armadio</h2>
  <div class="logo logo-dark" style="left:63px"><span class="mark"></span><span class="name">Casa<br>Lumo</span></div>
  <div class="abs body-text text-dark" style="left:60px;top:166px;width:244px">
    <p>L'arredamento della camera padronale. Sed ut perspiciatis unde omnis iste natus error sit voluptatem accusantium doloremque laudantium, totam rem aperiam, eaque ipsa quae ab illo inventore veritatis et quasi architecto beatae vitae dicta sunt explicabo. Nemo enim ipsam voluptatem quia voluptas sit aspernatur aut odit aut fugit.</p>
    <p>Sed ut perspiciatis unde omnis iste natus error sit voluptatem accusantium doloremque laudantium, totam rem aperiam, eaque ipsa quaea.</p>
  </div>
</section>

<!-- Slide 3 -->
<section class="slide bg-white" style="top:1398px">
  <div class="abs bg-brown" style="left:60px;top:0;width:642px;height:587px"></div>
  <h2 class="abs title title-lg" style="left:127px;top:28px">Camera<br>padronale</h2>
  <div class="abs photo" role="img" aria-label="Illustrazione di una camera da letto con letto blu e comodini" style="left:253px;top:215px;width:445px;height:311px;background:linear-gradient(180deg,#f1ece6 0%,#ece5dd 60%,#3e5566 75%,#e8e2db 100%)"></div>
  <div class="abs photo" role="img" aria-label="Illustrazione di una camera accogliente con letto, piante e specchio" style="left:457px;top:57px;width:444px;height:313px;background:radial-gradient(ellipse at 50% 60%,#e0c9bd 0%,#d8c2b4 55%,#d3bcad 100%)"></div>
  <div class="logo logo-dark" style="left:925px"><span class="mark"></span><span class="name">Casa<br>Lumo</span></div>
  <div class="abs body-text text-dark" style="left:740px;top:408px;width:244px">
    <p>Sed ut perspiciatis unde omnis iste natus error sit voluptatem accusantium doloremque laudantium, totam rem aperiam, eaque ipsa quae ab illo inventore veritatis et quasi architecto beatae vitae dicta suntea.</p>
  </div>
</section>

<!-- Slide 4 -->
<section class="slide bg-pink" style="top:2057px">
  <div class="abs bg-white" style="left:0;top:0;width:181px;height:587px"></div>
  <div class="logo logo-dark" style="left:63px"><span class="mark"></span><span class="name">Casa<br>Lumo</span></div>
  <h2 class="abs vertical-title" style="left:80px;bottom:134px">Cabina armadio</h2>
  <div class="abs body-text text-light" style="left:291px;top:90px;width:282px;text-align:left">
    <p>Sed ut perspiciatis unde omnis iste natus error sit voluptatem accusantium doloremque laud atium, totam rem aperiam, eaque ipsa quae ab illo inventore veritatis et quasi architecto beatae vitae dicta sptatemeaque ipsa quae ab illo inventore veriuntea.</p>
  </div>
  <div class="abs photo" role="img" aria-label="Illustrazione di una cabina armadio con scaffali, borse e camicie appese" style="left:614px;top:47px;width:352px;height:226px;background:linear-gradient(90deg,#d9d6d2 0%,#6c6c6c 25%,#777 75%,#d9d6d2 100%)"></div>
  <div class="abs photo" role="img" aria-label="Illustrazione della vetrina di un negozio di abbigliamento maschile" style="left:259px;top:313px;width:352px;height:227px;background:linear-gradient(180deg,#d8cfc4 0%,#c7c2bb 30%,#e6e3df 100%)"></div>
  <div class="abs body-text text-light" style="left:651px;top:353px;width:282px;text-align:left">
    <p>Sed ut perspiciatis unde omnis iste natus error sit voluptatem accusantium doloremque laud atium, totam rem aperiam, eaque ipsa quae ab illo inventore veritatis et quasi architecto beatae vitae dicta sptatemeaque ipsa quae ab illo inventore veriuntea.</p>
  </div>
</section>

<!-- Slide 5 -->
<section class="slide bg-brown" style="top:2716px">
  <div class="abs photo-plain" role="img" aria-label="Illustrazione di un bagno con vasca, specchio rotondo e mobile lavabo" style="left:0;top:75px;width:680px;height:512px;background:linear-gradient(180deg,#2e4a5e 0%,#2d475a 55%,#2a2f3a 75%,#8d5a33 88%,#7a4b2b 100%)"></div>
  <h2 class="abs title title-sm" style="left:725px;top:164px">Bagno padronale</h2>
  <div class="logo logo-light" style="left:925px"><span class="mark"></span><span class="name">Casa<br>Lumo</span></div>
  <div class="abs body-text text-light" style="left:725px;top:222px;width:262px">
    <p>Sed ut perspiciatis unde omnis iste natus error sit voluptatem accusantium dolor emque lauda ntium, totam rem aperiam, eaque ipsa quae ab illo inventore veritatis et quasi architecto beatae vitae dicta suntem accusantium dotea.</p>
    <p>Sed ut perspiciatis unde omnis iste natus error sit voluptatem accusantium dolor emque lauda ntium, totam rem aperiam, eaque ipsa quae ab illo inventore veritatis et quasi architectoea.</p>
  </div>
</section>

<!-- Slide 6 -->
<section class="slide bg-pink" style="top:3375px">
  <div class="abs bg-white" style="left:863px;top:0;width:181px;height:587px"></div>
  <div class="abs photo" role="img" aria-label="Illustrazione di un armadio aperto con abiti piegati, borse e grucce" style="left:60px;top:60px;width:502px;height:467px;background:linear-gradient(90deg,#f1d9ad 0%,#eccf9d 28%,#9a6c4f 30%,#8e634a 68%,#f1d9ad 70%,#ecd0a0 100%)"></div>
  <div class="abs body-text text-light" style="left:584px;top:122px;width:248px">
    <p>Sed ut perspiciatis unde omnis iste natus error sit voluptatem accusantium doloremque laud atium, totam rem aperiam, eaque ipsa quae ab illo inventore veritatis et quasi architecto beatae vitae dicta sptatemeaque ipsa quae ab illo inventore veriuntea.</p>
    <p>Sed ut perspiciatis unde omnis iste natus error sit voluptatem accusantium doloremque laud atium, totam rem aperiam, eaque ipsa quae ab illo inventore veritatis et quasi architecto beatae vitae dicta sptatemeaque ipsa quae ab illo inventore veriuntea.</p>
  </div>
  <div class="logo logo-dark" style="left:925px"><span class="mark"></span><span class="name">Casa<br>Lumo</span></div>
  <h2 class="abs vertical-title" style="left:940px;bottom:134px">Cabina armadio</h2>
</section>

</body>
</html>
```